Growing Wellness Company Needs an Amazing Cover for a series of Booklets

We are publishing our own series of booklets on health & wellness topics, called Vital Spark Primers and need an inspiring, modern design for the cover. We are beginning with the Title Diabetes: Type 2, but we will use this design for other titles later one.

SIZE:
This will be the front and back of a 8.5 x 5.5 booklet, plus 2 sample interior pages.

COLOR:
We are an industry leaders and prefer touse vibrant colors and designs to inspire our clients to change to a healthier lifestyle.

REQUIREMENTS:
I am attaching our Vital Spark logo, which needs to be on each cover, but does not need to be the focal point. You may you the words vital spark or just the b logo. The topic/title needs to be no lower than 1/2" from the top of the cover.

I'm attaching some samples of items I like, but please be creative!
If you would like to see some of our other in-house samples of publications send me a message and I'll show you. I will give detailed feedback so dive in and get creative!

FRONT COVER: 
1. Can you please make sure the title is in the top 1.5" of the page, i can't tell from this view. 
Type 2 Diabetes (1st line, bigger) 
A Simple Guide to Understanding & Controlling Your Blood Sugar (Second Row, much smaller) this can also be below the 1.5" line if it needs to be. 
3.We would like to see three shapes maybe toward the bottom with these words in them, one word per shape. inspire, equip, succeed 

IMAGE 
1. We would like you to leave a placeholder for an image, but would like to see different shapes, such as a rounded square or rectangle or a rectangle with two square corners and two rounded corners. 
2. Please play with some different border options as well,

BACKSIDE 
1. please put our information on the back side on the bottom, small. the information i will put in a file on the brief, the 2nd page has our address, phone, etc. 
2. Add our TA logo (attached as an image in the design brief)

Thanks! looking forward to what else you have. 

Reason: I want to give more time to get more/better designs in, i know this is a little more involved project.

Reason: Still not happy with designs, would like to see more.

Hello - thank you for submitting designs, the designs are getting a little too busy....here is a website I love the simplicity of...thanks!  http://www.brightmeadowcare.example   

Reason: We are getting closer to narrowing it down, I want to give the designers a few more days to tweak their designs, then i will ask the final 2 or 3 to submit a couple version of the inside pages. I will supply text for those so you know what you're working with. Thanks!

Target Market(s)

Our clients are adults, about 50/50 men & women in the age range from 20-70 with most being in their early 50's. from high school education up to professional degrees

Font styles to use
Serif
Sans Serif
Script

Colors
a64599
e34197
00a98f
9bcb3c
ffc214
f78f20
f37122
0492cd
6a439a

Requirements
Must have
• Eye catching, inspiring design that entices people to read our booklet:

I need a front and back cover and 2 interior page samples , we will be using more of an info graphic style inside possible with a few actual photographs

FRONT COVER REQUIREMENTS:
Title (must be no lower than 1.5" below the top)
Vital Spark Logo (attached in pink and green)
Thrive Allies' Logo

BACK COVER REQUIREMENTS:
a place for summary text
thrive allies contact information
a place for an item # (can be small, no barcode)
Nice to have
• the colors i chose are samples, does not need to include every color, each title we write will have a different color story

I can appreciate a white cover with some amazing art of pops of color, but i would also love a really rich color with subtle tone on tone things (see the navy blue cover picture)
Should not have
• boring colors, lots of pictures, typical booklet design

```html
<!DOCTYPE html>
<html lang="en">
<head>
<meta charset="utf-8">
<title>Type 2 Diabetes – Booklet Covers</title>
<link rel="stylesheet" href="https://fonts.googleapis.com/css2?family=Questrial&family=Poppins:wght@600&family=Oleo+Script&family=Abril+Fatface&display=swap">
<style>
  :root{
    --green:#9dc94c;
    --white:#ffffff;
    --frame-gray:#808184;
    --orange:#f6921e;
    --blue:#1565a9;
    --yellow:#f2ea2f;
    --magenta:#c90b7a;
    --pink:#ec008c;
    --navy:#2b3990;
    --ink:#333333;
    --word:#d6d6d6;
  }
  *{margin:0;padding:0;box-sizing:border-box}
  html,body{width:1200px;height:942px;overflow:hidden;background:var(--white)}
  .spread{position:relative;width:1200px;height:942px;font-family:"Questrial",sans-serif}
  .cover-label{position:absolute;top:20px;width:548px;text-align:center;font-size:24px;color:#222;letter-spacing:.5px}
  .cover{position:absolute;top:62px;width:548px;height:846px;overflow:hidden;background:var(--green)}
  .cover--back{left:33px}
  .cover--front{left:612px}
  .cover svg.art{position:absolute;inset:0}

  .summary{position:absolute;left:0;top:28px;width:548px;height:497px;color:var(--white);font-size:12.5px;line-height:16.5px;text-align:center;letter-spacing:.2px}
  .summary-edge{height:497px}
  .summary-edge--left{float:left;width:262px;shape-outside:polygon(0 0,242px 0,216px 16px,162px 91px,142px 192px,151px 277px,178px 354px,220px 426px,262px 497px,0 497px)}
  .summary-edge--right{float:right;width:286px;shape-outside:polygon(249px 0,286px 0,286px 497px,0 497px,34px 482px,129px 452px,272px 408px,272px 36px)}
  .summary p{margin:0}
  .summary p + p{text-indent:2.4em}

  .publisher{position:absolute;left:19px;top:768px;display:flex;gap:8px;color:var(--white)}
  .publisher-mark{width:42px;height:42px;background:var(--white);margin-top:2px}
  .publisher-info{font-size:6.5px;line-height:8px}
  .publisher-name{font-size:9px;font-weight:bold;margin-bottom:3px}
  .publisher-web{margin-top:3px;font-weight:bold}
  .item-number{position:absolute;left:305px;top:816px;font-size:8px;color:var(--white)}

  .title{position:absolute;left:0;width:548px;top:18px;text-align:center;font-family:"Poppins",sans-serif;font-weight:600;font-size:62px;letter-spacing:-3px;color:var(--ink);line-height:1}
  .title-num{color:var(--pink)}
  .subtitle{position:absolute;left:0;width:548px;top:95px;text-align:center;color:var(--white);font-family:"Oleo Script",cursive;font-size:16.5px}
  .subtitle .brace{font-family:"Questrial",sans-serif;font-size:34px;vertical-align:-6px;margin:0 4px}
  .word{position:absolute;font-family:"Abril Fatface",serif;color:var(--word);line-height:1}
  .word--inspire{left:318px;top:487px;font-size:62px}
  .word--equip{left:84px;top:662px;font-size:62px;transform:rotate(4deg)}
  .word--succeed{left:290px;top:736px;font-size:58px;transform:rotate(5deg)}
  .series-mark{position:absolute;left:10px;top:792px;color:var(--white);font-size:11px;line-height:12px;font-weight:bold}
</style>
</head>
<body>
<main class="spread">
  <div class="cover-label" style="left:33px">BACK COVER</div>
  <div class="cover-label" style="left:612px">FRONT COVER</div>

  <section class="cover cover--back">
    <svg class="art" viewBox="0 0 548 846" width="548" height="846">
      <g fill="var(--white)" stroke="var(--white)" stroke-width="60" stroke-linejoin="round">
        <path d="M262,525 C180,430 128,340 128,220 C128,70 240,-20 380,-20 C480,-20 560,40 600,120 L600,420 Z"/>
        <path d="M250,535 C200,420 120,300 0,280 L0,680 C100,670 190,600 250,545 Z"/>
        <path d="M275,540 C340,470 450,410 600,400 L600,760 C470,700 350,620 275,552 Z"/>
        <path d="M262,555 C200,620 80,700 0,720 L0,846 L460,846 C420,720 340,620 262,560 Z"/>
      </g>
      <g fill="var(--frame-gray)" stroke="var(--frame-gray)" stroke-width="34" stroke-linejoin="round">
        <path d="M262,525 C180,430 128,340 128,220 C128,70 240,-20 380,-20 C480,-20 560,40 600,120 L600,420 Z"/>
        <path d="M250,535 C200,420 120,300 0,280 L0,680 C100,670 190,600 250,545 Z"/>
        <path d="M275,540 C340,470 450,410 600,400 L600,760 C470,700 350,620 275,552 Z"/>
        <path d="M262,555 C200,620 80,700 0,720 L0,846 L460,846 C420,720 340,620 262,560 Z"/>
      </g>
      <path fill="var(--orange)" d="M262,525 C180,430 128,340 128,220 C128,70 240,-20 380,-20 C480,-20 560,40 600,120 L600,420 Z"/>
      <path fill="var(--blue)" d="M250,535 C200,420 120,300 0,280 L0,680 C100,670 190,600 250,545 Z"/>
      <path fill="var(--yellow)" d="M275,540 C340,470 450,410 600,400 L600,760 C470,700 350,620 275,552 Z"/>
      <path fill="var(--magenta)" d="M262,555 C200,620 80,700 0,720 L0,846 L460,846 C420,720 340,620 262,560 Z"/>
    </svg>

    <div class="summary">
      <div class="summary-edge summary-edge--left"></div>
      <div class="summary-edge summary-edge--right"></div>
      <p>Lorem ipsum dolor sit amet, consectetuer adipiscing elit. Aenean commodo ligula eget dolor. Aenean massa. Cum sociis natoque penatibus et magnis dis parturient montes, nascetur ridiculus mus. Donec quam felis, ultricies nec, pellentesque eu, pretium quis, sem. Nulla consequat massa quis enim. Donec pede justo, fringilla vel, aliquet nec, vulputate eget, arcu. In enim justo, rhoncus ut, imperdiet a, venenatis vitae, justo.</p>
      <p>Nullam dictum felis eu pede mollis pretium. Integer tincidunt. Cras dapibus. Vivamus elementum semper nisi. Aenean vulputate eleifend tellus. Aenean leo ligula, porttitor eu, consequat vitae, eleifend ac, enim. Aliquam lorem ante, dapibus in, viverra quis, feugiat a, tellus. Phasellus viverra nulla ut metus varius laoreet. Quisque rutrum. Aenean imperdiet. Etiam ultricies nisi vel augue. Curabitur ullamcorper ultricies nisi. Maecenas nec odio et ante tincidunt tempus. Donec vitae sapien ut libero venenatis faucibus.</p>
    </div>

    <div class="publisher">
      <div class="publisher-mark"></div>
      <div class="publisher-info">
        <div class="publisher-name">Thrive Allies LLC</div>
        <div>214 Linden Avenue</div>
        <div>P.O. Box 732</div>
        <div>Harlow, KS 67510</div>
        <div class="publisher-web">thrive-allies.example<br>555.014.2290</div>
      </div>
    </div>
    <div class="item-number">1234092193819</div>
  </section>

  <section class="cover cover--front">
    <svg class="art" viewBox="0 0 548 846" width="548" height="846">
      <defs>
        <linearGradient id="photoTone" x1="0" y1="0" x2="1" y2="1">
          <stop offset="0" stop-color="#e9dcc0"/>
          <stop offset=".5" stop-color="#d9b79a"/>
          <stop offset="1" stop-color="#f2f0ec"/>
        </linearGradient>
      </defs>
      <g fill="var(--white)" stroke="var(--white)" stroke-width="64" stroke-linejoin="round">
        <path d="M0,240 C90,215 230,220 280,290 C305,330 308,360 308,400 L308,608 L0,608 Z"/>
        <path d="M298,460 C298,420 330,400 380,400 C460,400 520,430 548,470 L548,618 L298,618 Z"/>
        <path d="M283,620 L283,790 C260,830 210,843 170,843 C110,843 68,790 68,720 C68,650 120,620 180,620 Z"/>
        <path d="M296,628 L548,628 L548,846 L320,846 C296,820 296,780 296,740 Z"/>
      </g>
      <g fill="var(--frame-gray)" stroke="var(--frame-gray)" stroke-width="34" stroke-linejoin="round">
        <path d="M0,240 C90,215 230,220 280,290 C305,330 308,360 308,400 L308,608 L0,608 Z"/>
        <path d="M298,460 C298,420 330,400 380,400 C460,400 520,430 548,470 L548,618 L298,618 Z"/>
        <path d="M283,620 L283,790 C260,830 210,843 170,843 C110,843 68,790 68,720 C68,650 120,620 180,620 Z"/>
        <path d="M296,628 L548,628 L548,846 L320,846 C296,820 296,780 296,740 Z"/>
      </g>
      <path fill="url(#photoTone)" role="img" aria-label="Photo of a smiling older couple embracing outdoors" d="M0,240 C90,215 230,220 280,290 C305,330 308,360 308,400 L308,608 L0,608 Z"/>
      <path fill="var(--pink)" d="M298,460 C298,420 330,400 380,400 C460,400 520,430 548,470 L548,618 L298,618 Z"/>
      <path fill="var(--orange)" d="M283,620 L283,790 C260,830 210,843 170,843 C110,843 68,790 68,720 C68,650 120,620 180,620 Z"/>
      <path fill="var(--navy)" d="M296,628 L548,628 L548,846 L320,846 C296,820 296,780 296,740 Z"/>
    </svg>

    <h1 class="title">Type <span class="title-num">2</span> Diabetes</h1>
    <p class="subtitle"><span class="brace">{</span>A Simple Guide to Understanding &amp; Controlling Your Blood Sugar<span class="brace">}</span></p>

    <span class="word word--inspire">inspire</span>
    <span class="word word--equip">equip</span>
    <span class="word word--succeed">succeed</span>

    <div class="series-mark">Vital<br>Spark</div>
  </section>
</main>
</body>
</html>
```